Financial Advisor Resource Firm needs business card design

Need business card design for company in Omaha NE called Tallowbrook Partners. We provide resources to financial advisors....workshop programs, retirement analysis, and insurance planning. I would like to see designs that use grays, greens, black, and white colors. The final design should communicate 'collaboration' and be simple yet attractive to financial planning clients. I will attached our logo and another picture of a puzzle piece coming together. I would like the incorporate the puzzle picture somehow, maybe on the back somehow, with color or just the gray scale....OR, the picture be the front of the card with 'Tallowbrook' definition on it (see upload) and then company logo, employee name, title, address on the back (see ppt uploaded). The following disclosure needs to be included somewhere- Advisory services offered through Marlowe Ridge Advisors, LLC.
Updates

I uploaded a svg and ai file of the logo

Target Market(s)

Financial planning clients and financial advisors....so pretty diverse age range of about 40-70.

Industry/Entity Type

Financial Planning

Contact Information for Business Card

Dennis K. Holloway, MBA
Founder/President
5727 E. Larkspur Avenue
Suite 418
Omaha, NE 68297
Phone- (402) 555-0147
Cell- (402) 555-0183
Fax- (402) 555-0129
email- dennis@tallowbrookgroup.example
web address- www.tallowbrookgroup.example

Colors
1b1b1b
474747
d3d3d3
ffffff
9bcb3c
abd036

Requirements
Must have
• Must include logo provided, must be 2 sided, and must have disclosure...all of these items listed in project description

```html
<!DOCTYPE html>
<html lang="en">
<head>
<meta charset="utf-8">
<title>Tallowbrook Partners – Business Card</title>
<link rel="stylesheet" href="https://fonts.googleapis.com/css2?family=Cinzel:wght@400;600&family=Open+Sans:wght@400&display=swap">
<style>
  :root {
    --page-bg: #dcdcdc;
    --brand-green: #8fc14c;
    --ink: #1b1b1b;
    --ink-soft: #474747;
    --rule: #b9b9b9;
    --icon: #8a8a8a;
    --paper: #ffffff;
  }
  * { margin: 0; padding: 0; box-sizing: border-box; }
  html, body { width: 1200px; height: 1200px; overflow: hidden; }
  body {
    background: var(--page-bg);
    display: flex;
    flex-direction: column;
    align-items: center;
    justify-content: center;
    gap: 60px;
    font-family: "Open Sans", Arial, sans-serif;
  }
  .card {
    width: 840px;
    height: 480px;
    position: relative;
    box-shadow: 0 6px 18px rgba(0,0,0,0.18);
  }
  /* Front */
  .card-front {
    background: var(--brand-green);
    display: flex;
    align-items: center;
    justify-content: center;
  }
  .front-wordmark {
    display: flex;
    align-items: center;
    gap: 18px;
    color: var(--paper);
    font-family: "Cinzel", Georgia, serif;
    font-weight: 400;
    font-size: 50px;
    letter-spacing: 1px;
  }
  .front-wordmark .mark-dot {
    width: 38px; height: 38px;
    border-radius: 50%;
    background: var(--paper);
  }
  /* Back */
  .card-back { background: var(--paper); }
  .back-wordmark {
    position: absolute;
    left: 40px; top: 152px;
    display: flex; align-items: center; gap: 9px;
    font-family: "Cinzel", Georgia, serif;
    font-weight: 400;
    font-size: 19px;
    white-space: nowrap;
    color: var(--ink);
  }
  .back-wordmark .mark-dot {
    width: 16px; height: 16px; border-radius: 50%;
    background: var(--brand-green);
    flex: none;
  }
  .divider {
    position: absolute;
    left: 352px; top: 108px;
    width: 1.5px; height: 110px;
    background: var(--rule);
  }
  .details {
    position: absolute;
    left: 384px; top: 86px;
    color: var(--ink);
  }
  .person-name {
    font-family: "Cinzel", Georgia, serif;
    font-weight: 600;
    font-size: 25px;
    line-height: 1.1;
    white-space: nowrap;
  }
  .person-title {
    font-size: 16px;
    color: var(--ink-soft);
    letter-spacing: 0.5px;
    margin-top: 2px;
  }
  .address {
    font-style: normal;
    font-size: 19px;
    line-height: 1.3;
    margin-top: 24px;
  }
  .contact-list {
    list-style: none;
    margin-top: 20px;
    font-size: 19px;
    line-height: 1.3;
  }
  .contact-list li {
    display: flex; align-items: center; gap: 12px;
    white-space: nowrap;
  }
  .contact-list svg {
    width: 18px; height: 18px;
    fill: none; stroke: var(--icon); stroke-width: 1.6;
    stroke-linecap: round; stroke-linejoin: round;
    flex: none;
  }
  .disclosure {
    position: absolute;
    left: 40px; right: 40px; bottom: 22px;
    font-size: 12px;
    color: var(--ink-soft);
    letter-spacing: 0.3px;
  }
</style>
</head>
<body>

<section class="card card-front" aria-label="Card front">
  <div class="front-wordmark">
    <span class="mark-dot"></span>
    <span class="brand-name">Tallowbrook Partners</span>
  </div>
</section>

<section class="card card-back" aria-label="Card back">
  <div class="back-wordmark">
    <span class="mark-dot"></span>
    <span class="brand-name">Tallowbrook Partners</span>
  </div>
  <div class="divider"></div>

  <div class="details">
    <div class="person-name">Dennis K. Holloway, MBA</div>
    <div class="person-title">FOUNDER/PRESIDENT</div>

    <address class="address">
      5727 E. Larkspur Avenue<br>
      Suite 418<br>
      Omaha, NE 68297
    </address>

    <ul class="contact-list">
      <li>
        <svg viewBox="0 0 18 18" aria-label="Mobile"><rect x="5" y="1.5" width="8" height="15" rx="1.5"/><line x1="8" y1="14" x2="10" y2="14"/></svg>
        (402) 555-0183
      </li>
      <li>
        <svg viewBox="0 0 18 18" aria-label="Phone"><path d="M4 2.5l3 3-1.6 2a9 9 0 0 0 5.1 5.1l2-1.6 3 3-1.7 1.7C9 16 2 9 2.8 4.2z"/></svg>
        (402) 555-0147
      </li>
      <li>
        <svg viewBox="0 0 18 18" aria-label="Fax"><rect x="2" y="7" width="14" height="9" rx="1"/><rect x="5" y="2" width="8" height="5"/><line x1="5" y1="10" x2="7" y2="10"/><line x1="9" y1="10" x2="13" y2="10"/><line x1="5" y1="13" x2="13" y2="13"/></svg>
        (402) 555-0129
      </li>
      <li>
        <svg viewBox="0 0 18 18" aria-label="Email"><rect x="1.5" y="4" width="15" height="10.5" rx="1"/><path d="M1.5 4.5l7.5 6 7.5-6"/></svg>
        dennis@tallowbrookgroup.example
      </li>
      <li>
        <svg viewBox="0 0 18 18" aria-label="Website"><path d="M7.5 10.5a3 3 0 0 0 4.2 0l3-3a3 3 0 0 0-4.2-4.2l-1 1"/><path d="M10.5 7.5a3 3 0 0 0-4.2 0l-3 3a3 3 0 0 0 4.2 4.2l1-1"/></svg>
        www.tallowbrookgroup.example
      </li>
    </ul>
  </div>

  <p class="disclosure">Advisory services offered through Marlowe Ridge Advisors, LLC.</p>
</section>

</body>
</html>
```